The Molar Ledger (Cover Design for Ebook)

I need a cool and exciting eBook cover for my new book, launching very soon!
I want it to stand out and appeal to young professionals with big dreams.
It should be dramatic and bold and avoid cliche or generic photos. Simple design will work as long as it relates to the message of the book. The content will provide ten years of experience from working in the field and achieving success.
Title: The Molar Ledger (at the top)
(Subheading Updated) The Habits to Wealth, Ambition and Freedom they don’t teach you in dental school
OR The secrets to success they don't teach you in dental school.
OR The Habits to Wealth, Ambition and Freedom
(smaller under title)
Author Updated: Dr K Fenwick (place at the bottom)
Updates

Target Market(s)

Ambitious young dentists
See instagram www.snapverse.net/themolarledger for a sense of the style that I think could work.

Font styles to use
Serif
Sans Serif

Colors

Designer to choose colors to be used in the design.

Requirements
Must have
• Eye catching and cool.
• Show the benefits of success. Money, freedom, luxury
• Clear title and subheading
Nice to have
• Subtle dental reference
• dimensions 1600x2400
Should not have
• Boring photos of dentist/patients, dental clinic, teeth etc,

```html
<!DOCTYPE html>
<html lang="en">
<head>
<meta charset="utf-8">
<title>The Molar Ledger — Ebook Cover</title>
<link rel="stylesheet" href="https://fonts.googleapis.com/css2?family=Cinzel:wght@400&family=Arimo:wght@400&display=swap">
<style>
  :root {
    --paper: #ffffff;
    --gold-deep: #b97a2c;
    --gold-mid: #d6a84e;
    --gold-light: #f1e08c;
    --ink: #474747;
    --ink-dark: #4a4948;
  }
  * { margin: 0; padding: 0; box-sizing: border-box; }
  html, body { width: 800px; height: 1200px; overflow: hidden; background: var(--paper); }
  .cover {
    position: relative;
    width: 800px;
    height: 1200px;
    background: var(--paper);
    overflow: hidden;
  }
  .title-line {
    position: absolute;
    left: 0;
    width: 800px;
    text-align: center;
    font-family: "Cinzel", "Trajan Pro", serif;
    font-weight: 400;
    text-transform: uppercase;
    line-height: 1;
    white-space: nowrap;
    background: linear-gradient(180deg, var(--gold-deep) 0%, var(--gold-mid) 25%, var(--gold-light) 60%, var(--gold-mid) 82%, var(--gold-deep) 100%);
    -webkit-background-clip: text;
    background-clip: text;
    color: transparent;
  }
  .title-article { top: 44px; font-size: 90px; letter-spacing: 2px; }
  .title-main { font-size: 146px; letter-spacing: 2px; }
  .title-main--first { top: 130px; }
  .title-main--second { top: 258px; }
  .tooth-art {
    position: absolute;
    left: 46px;
    top: 448px;
    width: 354px;
    height: 512px;
    border-radius: 46% 46% 30% 30% / 30% 30% 22% 22%;
    background: radial-gradient(ellipse at 50% 40%, #fffdf4 0%, #f8eccb 60%, #ecd193 100%);
  }
  .subtitle {
    position: absolute;
    right: 96px;
    top: 552px;
    text-align: right;
    font-family: "Arimo", Arial, sans-serif;
    font-size: 44px;
    line-height: 52px;
    letter-spacing: 1px;
    word-spacing: 6px;
    color: var(--ink);
  }
  .author-band {
    position: absolute;
    left: 0;
    top: 1056px;
    width: 800px;
    height: 144px;
    background: linear-gradient(180deg, var(--gold-deep) 0%, var(--gold-mid) 35%, var(--gold-light) 75%, var(--gold-light) 100%);
    display: flex;
    align-items: center;
    justify-content: center;
  }
  .author-name {
    font-family: "Cinzel", "Trajan Pro", serif;
    font-weight: 400;
    font-size: 92px;
    letter-spacing: 3px;
    color: var(--ink-dark);
    line-height: 1;
    padding-top: 8px;
    white-space: nowrap;
  }
</style>
</head>
<body>
  <main class="cover">
    <h1 class="title">
      <span class="title-line title-article">The</span>
      <span class="title-line title-main title-main--first">Molar</span>
      <span class="title-line title-main title-main--second">Ledger</span>
    </h1>
    <div class="tooth-art" role="img" aria-label="Gold line drawing of a single molar tooth outline"></div>
    <p class="subtitle">The Habits<br>to Wealth,<br>Ambition<br>and Freedom</p>
    <footer class="author-band">
      <p class="author-name">KIT FENWICK</p>
    </footer>
  </main>
</body>
</html>
```